Wealth management firm needs a business card design

Using my logo, create a business card that covers all of the regulatory wordings that I need. It must have - Registered Office 5-7 Pellinore Court, Edinburgh, EH9 2QW. Registered in Scotland under number SC738204. Corvell Wealth Management Ltd is an appointed representative of Quintor wealth management Ltd, which is authorised and regulated by the Monetary Standards Council.

Target Market(s)

professional clients

Industry/Entity Type

finance

Contact Information for Business Card

Corvell Wealth Management, Rupert Ashdown-Kerr, Director, 9 Tanner Row, Edinburgh, EH2 4NP. 07812 455 193, rupert.ashdown-kerr@corvellwealth.example , www.corvellwealth.example

Font styles to use
Serif

Colors
0054AA
0677BA
7BADD7
CADEEF
E8F1F8

Requirements
Must have
• regulatory wording in small text at bottom

```html
<!DOCTYPE html>
<html lang="en">
<head>
<meta charset="utf-8">
<title>Corvell Wealth Management – Business Card</title>
<link rel="stylesheet" href="https://fonts.googleapis.com/css2?family=Merriweather:wght@400;700&display=swap">
<style>
  :root {
    --stage: #4b4b4b;
    --brand-blue: #4176bd;
    --brand-blue-dark: #2f5fa8;
    --emboss-light: #5a8bcc;
    --emboss-dark: #3563a6;
    --ink: #1d1d1f;
    --muted-ink: #4a4a52;
    --paper: #fdfdff;
    --night: #04050d;
  }
  * { box-sizing: border-box; margin: 0; padding: 0; }
  html, body { width: 1200px; height: 780px; overflow: hidden; }
  body {
    background: var(--stage);
    font-family: "Merriweather", Georgia, serif;
    display: flex;
    align-items: center;
    justify-content: center;
    gap: 40px;
  }
  .card {
    width: 540px;
    height: 310px;
    border-radius: 26px;
    overflow: hidden;
    position: relative;
  }

  /* Back side */
  .card-back {
    background: var(--brand-blue);
    display: flex;
    flex-direction: column;
    align-items: center;
    justify-content: center;
    gap: 22px;
  }
  .back-mark {
    width: 96px; height: 96px;
    border-radius: 50%;
    background: var(--brand-blue);
    box-shadow: inset 2px 2px 3px var(--emboss-dark), inset -2px -2px 3px var(--emboss-light);
  }
  .back-name {
    font-size: 28px;
    font-weight: 400;
    color: var(--brand-blue);
    text-shadow: -1px -1px 1px var(--emboss-dark), 1px 1px 1px var(--emboss-light);
    white-space: nowrap;
  }

  /* Front side */
  .card-front { background: var(--paper); }
  .front-brand {
    position: absolute;
    left: 14px; top: 112px;
    width: 180px;
    display: flex;
    flex-direction: column;
    align-items: center;
    gap: 12px;
  }
  .front-mark {
    width: 34px; height: 34px;
    border-radius: 50%;
    background: var(--brand-blue);
  }
  .front-name {
    font-size: 9.5px;
    color: var(--ink);
    white-space: nowrap;
  }
  .divider {
    position: absolute;
    left: 202px; top: 48px;
    width: 1.5px; height: 160px;
    background: var(--brand-blue-dark);
  }
  .contact {
    position: absolute;
    left: 218px; top: 40px;
    width: 310px;
    color: var(--ink);
  }
  .person-name {
    font-size: 19px;
    font-weight: 700;
    color: var(--brand-blue);
    white-space: nowrap;
  }
  .person-role { font-size: 12px; margin: 3px 0 10px 12px; }
  .contact-list { list-style: none; margin-left: 20px; }
  .contact-list li {
    font-size: 10px;
    line-height: 17px;
    display: flex;
    align-items: center;
    gap: 6px;
    white-space: nowrap;
  }
  .contact-list svg { width: 10px; height: 10px; fill: var(--brand-blue); flex: none; }
  .address { font-size: 11px; line-height: 16px; margin: 10px 0 0 36px; }
  .regulatory {
    position: absolute;
    left: 22px; top: 222px;
    width: 360px;
    font-size: 6.3px;
    line-height: 9px;
    color: var(--muted-ink);
  }
  .front-bands { position: absolute; left: 0; bottom: 0; width: 540px; height: 62px; }
</style>
</head>
<body>
  <section class="card card-back" aria-label="Business card, back">
    <div class="back-mark"></div>
    <p class="back-name">Corvell Wealth Management Ltd</p>
  </section>

  <section class="card card-front" aria-label="Business card, front">
    <div class="front-brand">
      <div class="front-mark"></div>
      <p class="front-name">Corvell Wealth Management Ltd</p>
    </div>
    <div class="divider"></div>
    <div class="contact">
      <h1 class="person-name">Rupert Ashdown-Kerr</h1>
      <p class="person-role">Director</p>
      <ul class="contact-list">
        <li><svg viewBox="0 0 24 24"><path d="M6.6 10.8a15.1 15.1 0 0 0 6.6 6.6l2.2-2.2a1 1 0 0 1 1-.25 11.4 11.4 0 0 0 3.6.57 1 1 0 0 1 1 1V20a1 1 0 0 1-1 1A17 17 0 0 1 3 4a1 1 0 0 1 1-1h3.5a1 1 0 0 1 1 1c0 1.25.2 2.45.57 3.57a1 1 0 0 1-.25 1z"/></svg>07812 455 193</li>
        <li><svg viewBox="0 0 24 24"><path d="M2 5h20v14H2z"/><path d="M3 6l9 7 9-7v-1H3z" fill="#fff"/></svg>rupert.ashdown-kerr@corvellwealth.example</li>
        <li><svg viewBox="0 0 24 24"><circle cx="12" cy="12" r="10"/><path d="M2 12h20M12 2c3 3 3 17 0 20M12 2c-3 3-3 17 0 20" stroke="#fff" stroke-width="1.6" fill="none"/></svg>www.corvellwealth.example</li>
      </ul>
      <p class="address">9 Tanner Row,<br>Edinburgh, EH2 4NP</p>
    </div>
    <p class="regulatory">Registered Office 5-7 Pellinore Court, Edinburgh, EH9 2QW. Registered in Scotland under number SC738204. Corvell Wealth Management Ltd is an appointed representative of Quintor wealth management Ltd, which is authorised and regulated by the Monetary Standards Council.</p>
    <svg class="front-bands" viewBox="0 0 540 62" aria-hidden="true">
      <rect x="0" y="34" width="540" height="8" fill="var(--brand-blue)"/>
      <rect x="0" y="46" width="540" height="16" fill="var(--brand-blue)"/>
      <polygon points="402,12 540,0 540,46 398,46" fill="var(--night)"/>
    </svg>
  </section>
</body>
</html>
```